Real Estate Company Looking for Business Card Designs for 3 Executives

Hello!
Thanks so much for considering our project! We are a real estate investment company located in Edmonton, Alberta called Marlbeck Group of Companies. We invest/develop both commercial and residential real estate and are looking to create 3 DOUBLE-SIDED business cards for 3 top executives in the company! (for some reason it won't let us select the double-sided option, but yes, the cards are double sided and would be happy to tip extra)

We have certain guidelines that we want our business cards to for sure follow - the back of the Business card has to be the Black Background Version of the Logo which has already been designed and linked as a file (first file). We want the entire back of the card to simply just be the black background logo. In terms of the front of the card, would like to see a smaller version of the white background logo (linked as the second file) in the top left hand corner - of course, feel free to get creative and we can make revisions together along the way! and Then after that, just text. We want the card to be sharp, clean, easy on the eyes and highly professional looking. We would like the card to include the Full name of the Company (Marlbeck Group of Companies), Name of the Person, Title, Phone, Email. If possible please provide the front part of the card for 3 people:

1) Marlbeck Group of Companies, Lena Okafor, Chief Financial Officer, 780-555-0162, lenaokafor@marlbeckgroup.example

2) Marlbeck Group of Companies, Tobias Okafor, Chief Executive Officer, 780-555-0148, tobiasokafor@marlbeckgroup.example

3) Marlbeck Group of Companies, Rui Dalton, Chief Operations Officer, 587-555-0193, ruidalton@marlbeckgroup.example

Thank you so much for considering our project & we look forward to seeing your designs!

```html
<!DOCTYPE html>
<html lang="en">
<head>
<meta charset="utf-8">
<title>Marlbeck Group of Companies — Business Cards</title>
<link rel="stylesheet" href="https://fonts.googleapis.com/css2?family=Arimo:wght@400;700&display=swap">
<style>
  :root {
    --page: #e6e6e6;
    --card: #2f2f2f;
    --ink: #ffffff;
    --ink-soft: #e8e8e8;
    --emboss: #4a4a4a;
    --tree: #f4f4f4;
  }
  * { box-sizing: border-box; margin: 0; padding: 0; }
  html, body {
    width: 1200px; height: 801px; overflow: hidden;
    background: var(--page);
    font-family: "Arimo", Arial, sans-serif;
  }
  .sheet {
    width: 1200px; height: 801px;
    display: flex; align-items: center; justify-content: center; gap: 40px;
  }
  .card {
    position: relative;
    width: 560px; height: 320px;
    background: var(--card);
    overflow: hidden;
  }
  /* Front */
  .tree-art {
    position: absolute; top: 0; right: 0;
    width: 250px; height: 320px;
    background: linear-gradient(90deg, rgba(244,244,244,0.15) 0%, rgba(244,244,244,0.55) 45%, var(--tree) 100%);
  }
  .front-brand {
    position: absolute; left: 38px; top: 92px;
    color: var(--ink);
    font-size: 13px; font-weight: 400;
    letter-spacing: 9px;
    text-transform: uppercase;
  }
  .identity {
    position: absolute; left: 92px; top: 150px;
    color: var(--ink);
  }
  .identity .name {
    font-size: 19px; font-weight: 700; letter-spacing: 0.5px;
    text-transform: uppercase;
  }
  .identity .title {
    font-size: 15px; font-weight: 400; color: var(--ink-soft);
    margin-top: 2px;
  }
  .contact {
    list-style: none; margin-top: 22px;
    font-size: 15px; color: var(--ink-soft);
  }
  .contact li { display: flex; align-items: center; gap: 10px; line-height: 22px; }
  .contact svg { width: 12px; height: 12px; flex: none; }
  /* Back */
  .back-brand {
    position: absolute; inset: 0;
    display: flex; align-items: center; justify-content: center;
    color: var(--emboss);
    font-size: 30px; font-weight: 400;
    letter-spacing: 16px;
    text-transform: uppercase;
    padding-left: 16px;
  }
</style>
</head>
<body>
<main class="sheet">
  <section class="card card--front" aria-label="Business card front">
    <div class="tree-art" role="img" aria-label="White silhouette of a bare tree trunk with branches reaching to the right"></div>
    <p class="front-brand">Marlbeck</p>
    <div class="identity">
      <h1 class="name">Lena Okafor</h1>
      <p class="title">Chief Financial</p>
      <ul class="contact">
        <li>
          <svg viewBox="0 0 12 12" aria-hidden="true"><path d="M3 1 L5 3.5 L4 5 Q5 7 7 8 L8.5 7 L11 9 L10 11 Q4 11 1 5 Q1 2 3 1 Z" fill="#ffffff"/></svg>
          <span>780-555-0162</span>
        </li>
        <li>
          <svg viewBox="0 0 12 12" aria-hidden="true"><rect x="0.8" y="2.2" width="10.4" height="7.6" fill="none" stroke="#ffffff" stroke-width="1.1"/><path d="M0.8 2.4 L6 6.6 L11.2 2.4" fill="none" stroke="#ffffff" stroke-width="1.1"/></svg>
          <span>lenaokafor@marlbeckgroup.example</span>
        </li>
      </ul>
    </div>
  </section>

  <section class="card card--back" aria-label="Business card back">
    <p class="back-brand">Marlbeck</p>
  </section>
</main>
</body>
</html>
```